Vehicle Signage Design for a Renovation Company

We're a renovation company specialising in Home Renovations. The final design should communicate trust, credibility, and confidence. We need vehicle signage designed for our company utes (see attachment) / for our grey ute with the canopy/ and white use withou the canopyI've also attached our existing designs for the current vehicles (van and hatch back) to give you an idea of what we're after.In terms of content, there isn't much requirement for this due to the limited space on the ute - but happy to hear ideas on this.We've tried designing it ourselves - see attachment, but not happy with the result, would like more variations and ideas.Check out our website www.kestrelrenovations.co.nz for ideas on our branding/ style.
Updates

Target Market(s)

Home Owners

Industry/Entity Type

Residential Construction

Font styles to use
Sans Serif

Colors
3276b5
0355a3
33a6d7
3aa7d7
ffffff

Requirements
Must have
• Logo, Call to Action (website and number), Headline
Nice to have
• Strong sharp lines, a clean/sleek look
• It would be nice to have our offer on there (free design plans) / but we know space is limited

```html
<!DOCTYPE html>
<html lang="en">
<head>
<meta charset="utf-8">
<title>Kestrel Home Renovations – Ute Wrap</title>
<link href="https://fonts.googleapis.com/css2?family=Lato:wght@700;900&display=swap" rel="stylesheet">
<style>
  :root {
    --navy: #1d2c86;
    --brand-blue: #0355a3;
    --bright-blue: #3276b5;
    --charcoal: #2f3033;
    --silver: #c9ccd1;
    --white: #ffffff;
    --page: #ffffff;
  }
  html, body {
    margin: 0;
    width: 1200px;
    height: 1043px;
    overflow: hidden;
    background: var(--page);
    font-family: "Lato", sans-serif;
  }
  .canvas { position: relative; width: 1200px; height: 1043px; }
  .wrap-panel { position: absolute; width: 908px; height: 240px; }
  .wrap-panel--driver { left: 28px; top: 160px; }
  .wrap-panel--passenger { left: 264px; top: 640px; }
  .band-blue { fill: url(#blueFade); }
  .band-dark { fill: var(--charcoal); }
  .band-silver { fill: var(--silver); }
  .web-address { fill: var(--white); font-weight: 700; font-size: 27px; }
  .brand-name { fill: var(--white); font-weight: 900; font-size: 82px; }
  .brand-tagline { fill: var(--white); font-weight: 700; font-size: 20px; letter-spacing: 0.5px; }
  .phone { fill: var(--white); font-weight: 900; font-size: 50px; }
  .offer { fill: var(--white); font-weight: 700; font-size: 25px; }
  .offer-arrow { fill: none; stroke: var(--white); stroke-width: 2.5; stroke-linecap: round; }
</style>
</head>
<body>
<div class="canvas">
  <svg width="0" height="0" style="position:absolute">
    <defs>
      <linearGradient id="blueFade" x1="0" y1="0" x2="1" y2="1">
        <stop offset="0" stop-color="var(--brand-blue)"/>
        <stop offset="0.6" stop-color="var(--navy)"/>
        <stop offset="1" stop-color="#16206a"/>
      </linearGradient>
    </defs>
  </svg>

  <!-- Driver side: vehicle faces right -->
  <svg class="wrap-panel wrap-panel--driver" viewBox="0 0 1135 300">
    <g class="wrap-bands">
      <polygon class="band-blue" points="0,40 420,5 1135,148 1060,300 0,300"/>
      <polygon class="band-silver" points="0,165 540,300 0,300"/>
      <polygon class="band-dark" points="0,75 420,60 1060,300 540,300 0,165"/>
    </g>
    <text class="web-address" x="95" y="62" transform="rotate(8 95 62)">kestrelrenovations.co.nz</text>
    <text class="brand-name" x="515" y="118" transform="rotate(8 515 118)">Kestrel</text>
    <text class="brand-tagline" x="665" y="185" transform="rotate(8 665 185)">HOME RENOVATIONS</text>
    <text class="phone" x="515" y="215" transform="rotate(8 515 215)">0800 451 726</text>
    <g class="offer-group" text-anchor="middle">
      <text class="offer" x="950" y="170">FREE</text>
      <text class="offer" x="950" y="197">Design</text>
      <text class="offer" x="950" y="224">Plans</text>
    </g>
    <path class="offer-arrow" d="M940 240 C935 262 900 264 864 258 M874 250 L862 258 L874 265"/>
  </svg>

  <!-- Passenger side: vehicle faces left -->
  <svg class="wrap-panel wrap-panel--passenger" viewBox="0 0 1135 300">
    <g class="wrap-bands" transform="translate(1135 0) scale(-1 1)">
      <polygon class="band-blue" points="0,40 420,5 1135,148 1060,300 0,300"/>
      <polygon class="band-silver" points="0,165 540,300 0,300"/>
      <polygon class="band-dark" points="0,75 420,60 1060,300 540,300 0,165"/>
    </g>
    <text class="web-address" x="1052" y="66" text-anchor="end" transform="rotate(-8 1052 66)">kestrelrenovations.co.nz</text>
    <text class="brand-name" x="250" y="172" transform="rotate(-8 250 172)">Kestrel</text>
    <text class="brand-tagline" x="390" y="200" transform="rotate(-8 390 200)">HOME RENOVATIONS</text>
    <text class="phone" x="292" y="264" transform="rotate(-8 292 264)">0800 451 726</text>
    <g class="offer-group" text-anchor="middle">
      <text class="offer" x="180" y="135">FREE</text>
      <text class="offer" x="180" y="162">Design</text>
      <text class="offer" x="180" y="189">Plans</text>
    </g>
    <path class="offer-arrow" d="M196 205 C198 240 230 258 280 255 M270 248 L282 255 L271 262"/>
  </svg>
</div>
</body>
</html>
```